Custom Die cut yard sign

Hi!

I would love to get really eye catching creative here with some window cleaning die cut signs!

I would like the main words to stand out of just saying, "Window Cleaning"

My phone number: 612-555-0143
Website: BrindlewayMN.com

My logo but it can be small as I want the "Window Cleaning and Phone number to really pop.

It can be a creative for implying window cleaning! Die cut so maybe water? Light? Windows outlines, squeegee? I don't know it's for residential window cleaning!

Attached is my logo and the template for the die cut sign.

Thanks!

```html
<!DOCTYPE html>
<html lang="en">
<head>
<meta charset="utf-8">
<title>Window Cleaning Yard Sign</title>
<link rel="stylesheet" href="https://fonts.googleapis.com/css2?family=Montserrat:wght@700;800&display=swap">
<style>
  :root {
    --backdrop: #1c1c1d;
    --navy: #16294f;
    --glass-light: #c3dfe8;
    --glass-mid: #9fcfdc;
    --glass-deep: #6fb7c8;
    --phone-start: #1e8ac8;
    --phone-end: #1d5f92;
    --lime: #8cc63f;
    --sky: #3aa3d9;
    --white: #ffffff;
  }
  html, body {
    margin: 0;
    width: 1200px;
    height: 943px;
    overflow: hidden;
    background: var(--backdrop);
  }
  .canvas {
    position: relative;
    width: 1200px;
    height: 943px;
    font-family: "Montserrat", sans-serif;
  }
  .sign {
    position: absolute;
    left: 78px;
    top: 70px;
    width: 1028px;
    height: 772px;
    overflow: hidden;
    background:
      radial-gradient(ellipse at 70% 45%, var(--glass-light) 0%, var(--glass-mid) 55%, var(--glass-deep) 100%);
    box-shadow: 8px 8px 0 #000;
  }
  .sign-art {
    position: absolute;
    inset: 0;
  }
  .headline {
    position: absolute;
    left: 0;
    width: 1028px;
    margin: 0;
    text-align: center;
    color: var(--navy);
    font-weight: 800;
    line-height: 1;
  }
  .headline--window {
    top: 58px;
    font-size: 168px;
    letter-spacing: 2px;
  }
  .headline--cleaning {
    top: 228px;
    font-size: 122px;
    font-weight: 700;
    letter-spacing: 4px;
  }
  .phone {
    position: absolute;
    left: 242px;
    top: 375px;
    width: 543px;
    height: 70px;
    background: linear-gradient(90deg, var(--phone-start), var(--phone-end));
    color: var(--white);
    font-weight: 700;
    font-size: 70px;
    line-height: 70px;
    text-align: center;
    letter-spacing: 1px;
  }
  .brand {
    position: absolute;
    left: 0;
    width: 1028px;
    top: 549px;
    text-align: center;
    color: var(--white);
    font-weight: 800;
    font-size: 38px;
    line-height: 1;
    letter-spacing: 1px;
  }
  .website {
    position: absolute;
    right: 70px;
    top: 688px;
    color: var(--navy);
    font-weight: 700;
    font-size: 54px;
    line-height: 1;
    letter-spacing: 1px;
  }
</style>
</head>
<body>
<div class="canvas">
  <div class="sign">
    <svg class="sign-art" width="1028" height="772" viewBox="0 0 1028 772">
      <defs>
        <linearGradient id="squeegeeTone" x1="0" y1="0" x2="1" y2="1">
          <stop offset="0" stop-color="#f3e7b0"/>
          <stop offset="0.55" stop-color="#4fb0e0"/>
          <stop offset="1" stop-color="#2a8fcf"/>
        </linearGradient>
      </defs>
      <polygon class="squeegee-photo" role="img" aria-label="Photo of a squeegee wiping a wet window pane"
               points="1028,165 1028,400 875,522 840,480 990,250" fill="url(#squeegeeTone)" opacity="0.85"/>
      <path class="arc-band" d="M0 724 Q520 380 1028 665 L1028 772 L0 772 Z" fill="var(--navy)"/>
      <path class="arc-field" d="M112 772 Q520 440 1028 690 L1028 772 Z" fill="var(--lime)"/>
      <circle class="brand-dot" cx="514" cy="506" r="34" fill="var(--sky)"/>
    </svg>
    <h1 class="headline headline--window">WINDOW</h1>
    <h2 class="headline headline--cleaning">CLEANING</h2>
    <div class="phone">612-555-0143</div>
    <div class="brand">Brindleway</div>
    <div class="website">www.BrindlewayMN.com</div>
  </div>
</div>
</body>
</html>
```